Fence Contractor Website Design

We are working with Yardline Works. They are a local fencing and automatic gate installer and in need of a new website design.
Some sites to use for inspiration:
https://brambleridgefence.example
https://marlowfence.example
https://www.tidewelldecksandfence.example
https://www.postwrightinc.example
Thank you for taking the time to consider designing a website for us. We are web developers based in Stockton, CA, USA. Most of our projects go through the same process. Understanding this process may help you win a project with us. We custom-code all of our websites in-house. We don’t have any requirements as to what tools you use for your design, but we prefer Figma files. For any design that we label as four-stars, we send it to the client for review. The client picks the final design they want us to use. Once we complete this process, we will continue to show additional clients all the four-star sites and purchase them later. Your designs will have multiple chances to sell. For better chances of success, we ask that you follow these guidelines.
IMAGES:
If you use any images or icons in the design, we ask that you have a link to the asset so we can purchase the image/icon. Most of the designs we submit do not have the customer’s images on them unless they have some great images. Be creative; show us the feeling you are trying to portray with your image choices. Use any royalty-free site you choose. We subscribe to Varnelle and mainly use their images, but we can purchase images outside of Varnelle.
PLEASE NOTE: we will not submit designs to clients with watermarks on the images.
FONTS:
We ask that you identify the fonts used in the design. This can be done in a message if you want. We typically use Google Fonts and Varnelle Fonts.
CONTENT:
We're always open to different content and ideas. We often submit designs with stock images so the client can see our vision. We typically take pictures after the website launch to use their images with our vision. Lorem Ipsum is fine for paragraphs, but we ask that you write the headers in correct English. We want to be able to show the vision and identify the sections of the website.
INSPIRATION:
We typically add a couple of links in the brief of websites we like to help you get started in your design.
REVISIONS:
We do not often ask for revisions of the designs unless we see something in the design that may not appeal to the client. If there are slight changes that we want to make, we do that in the development process.
FEEDBACK:
We rarely give feedback on designs during the design process. We are working on many website projects and do not have the time to provide feedback. We usually respond if your request is well thought out and asks specific questions, but a note asking “feedback, please” usually goes unanswered.

```html
<!DOCTYPE html>
<html lang="en">
<head>
<meta charset="utf-8">
<title>Yardline Works – Fencing &amp; Gates</title>
<link href="https://fonts.googleapis.com/css2?family=Russo+One&family=Poppins:wght@400;500;600;700&display=swap" rel="stylesheet">
<style>
:root{
  --red:#e3202a;
  --navy:#1c2a4a;
  --navy-deep:#17223d;
  --ink:#1d2433;
  --text:#4a505c;
  --soft:#f3f6fb;
  --pink:#f9d3d6;
  --grey-hex:#c5c9d1;
  --stage:#eceef2;
  --line:#dde1e8;
  --white:#fff;
}
*{box-sizing:border-box;margin:0;padding:0}
html,body{width:1200px;height:3141px;overflow:hidden}
body{position:relative;background:var(--stage);font-family:"Poppins",sans-serif;color:var(--text)}
.display{font-family:"Russo One",sans-serif;color:var(--ink);text-transform:uppercase;letter-spacing:.5px;font-weight:400}
.display em{font-style:normal;color:var(--red)}
.btn{display:inline-block;background:var(--navy);color:#fff;font-size:7px;font-weight:600;text-transform:uppercase;padding:6px 12px;border-radius:2px;letter-spacing:.4px}
.hex{clip-path:polygon(25% 3%,75% 3%,100% 50%,75% 97%,25% 97%,0 50%)}
.hexv{clip-path:polygon(50% 0,100% 25%,100% 75%,50% 100%,0 75%,0 25%)}
p{font-size:7.5px;line-height:1.55}

/* ========== desktop view ========== */
.view-desktop{position:absolute;left:152px;top:549px;width:800px;height:3143px;background:var(--white);overflow:hidden;transform:scale(.80875);transform-origin:0 0;border-radius:14px}
.container{position:relative;width:590px;margin:0 auto;height:100%}
section,footer{position:relative;overflow:hidden}

.site-header{height:50px;background:#fff;position:relative;z-index:3;overflow:visible}
.brand{position:absolute;left:85px;top:0;width:110px;height:92px;background:#fff;border-radius:0 0 50px 50px;display:flex;align-items:center;justify-content:center;gap:5px;box-shadow:0 3px 8px rgba(0,0,0,.12)}
.brand .dot{width:10px;height:10px;background:var(--red);border-radius:50%;flex:none}
.brand span{font-family:"Russo One",sans-serif;font-size:11px;color:var(--navy);line-height:1.1;width:62px}
.nav{position:absolute;left:250px;top:0;height:50px;display:flex;align-items:center;gap:17px;font-size:7px;font-weight:500;color:var(--ink)}
.nav .active{color:var(--red);text-decoration:underline}
.nav .phone{display:flex;align-items:center;gap:4px;margin-left:10px}
.nav .btn{margin-left:16px;padding:7px 14px}

.hero{height:330px}
.hero-photo{position:absolute;inset:0;background:linear-gradient(110deg,#2a2f2a 0%,#3f4a3c 35%,#1f2320 60%,#4d5a48 100%)}
.hero-content{position:relative;text-align:center;padding-top:100px}
.hero h1{font-family:"Russo One",sans-serif;font-weight:400;color:#fff;font-size:29px;line-height:1.08;text-transform:uppercase}
.hero h1 em{font-style:normal;color:var(--red)}
.hero .btn{background:#fff;color:var(--navy);margin-top:10px}

.split{height:385px}
.split .copy{position:absolute;left:0;top:95px;width:255px}
.split h2{font-size:21px;margin-bottom:14px;line-height:1}
.split p{margin-bottom:10px}
.split .btn{margin-top:6px}
.split-photo{position:absolute;left:335px;top:55px;width:255px;height:225px;background:linear-gradient(140deg,#7fa7c9,#c7a877 60%,#5b6a55)}
.deco{position:absolute}
.deco.pink{background:var(--pink)}
.deco.grey{background:var(--grey-hex)}
.badge-20{position:absolute;left:300px;top:170px;width:64px;height:70px;background:var(--red);color:#fff;font-family:"Russo One",sans-serif;font-size:20px;display:flex;align-items:center;justify-content:center}
.badge-label{position:absolute;left:300px;top:248px;font-family:"Russo One",sans-serif;font-size:9px;line-height:1.15;color:var(--ink)}

.sec-title{text-align:center;font-size:19px;display:flex;align-items:center;justify-content:center;gap:8px}
.sec-title::before,.sec-title::after{content:"";width:14px;height:1px;background:#b9bdc6}

.services{height:593px;background:var(--soft)}
.services .sec-title{padding-top:48px}
.service-grid{display:grid;grid-template-columns:repeat(3,183px);gap:18px 20px;margin-top:14px}
.card-img{height:155px;position:relative}
.card h3{font-size:8.5px;font-weight:700;color:var(--ink);margin:9px 8px 2px}
.card h3.hot{color:var(--red)}
.card p{font-size:6.5px;margin:0 8px;line-height:1.4}
.arrow-dot{position:absolute;right:12px;bottom:12px;width:26px;height:26px;background:var(--red);display:flex;align-items:center;justify-content:center}
.center-btn{text-align:center;margin-top:16px}

.testimonials{height:383px}
.testimonials .sec-title{padding-top:40px}
.quote-photo{position:absolute;left:0;top:95px;width:210px;height:185px;background:radial-gradient(circle at 50% 50%,#e79a2c 0,#8a4a13 30%,#111b2f 70%)}
.quote{position:absolute;left:265px;top:112px;width:325px}
.quote .mark{font-family:"Russo One",sans-serif;color:var(--red);font-size:30px;line-height:.8}
.quote p{font-size:9px;line-height:1.6;margin-top:10px;color:#3d4350}
.author{position:relative;display:flex;align-items:center;gap:8px;margin-top:16px}
.avatar{width:30px;height:30px;border-radius:50%;background:linear-gradient(#d7a9a0,#8b5f5a);border:2px solid #f1c9cc;flex:none}
.author b{display:block;color:var(--red);font-size:7.5px}
.author small{font-size:7px}
.dots{display:flex;gap:4px}
.author .dots{position:absolute;left:160px;top:11px}
.dots i{width:8px;height:8px;border:1px solid #555;border-radius:50%}
.dots i.on{border-color:var(--red);background:radial-gradient(var(--red) 40%,transparent 45%)}

.works{height:413px;background:var(--soft)}
.works .sec-title{padding-top:48px}
.work{position:absolute;top:110px;height:165px}
.work .info{position:absolute;left:18px;bottom:-20px;width:210px;background:#fff;padding:10px 12px;box-shadow:0 2px 6px rgba(0,0,0,.08)}
.work h3{font-size:8px;font-weight:700;color:var(--red);line-height:1.2;margin-bottom:4px}
.work.alt h3{color:var(--ink)}
.work .info p{font-size:6px;line-height:1.4;width:160px}
.work .go{position:absolute;right:12px;bottom:12px;width:18px;height:18px;border-radius:50%;background:var(--red);display:flex;align-items:center;justify-content:center}
.works .center-btn{position:absolute;left:0;right:0;top:330px;margin:0}

.clients{height:300px;background:var(--soft)}
.clients .sec-title{padding-top:58px}
.clients .sec-title::before,.clients .sec-title::after{display:none}
.clients .sub{text-align:center;font-size:7.5px;color:var(--ink)}
.logo-row{display:flex;justify-content:space-between;margin-top:26px}
.logo-hex{width:110px;height:100px;background:#fff;display:flex;align-items:center;justify-content:center;gap:5px}
.logo-hex i{width:14px;height:14px;border-radius:50%}
.logo-hex span{font-family:"Russo One",sans-serif;font-size:10px;color:#555}
.pager{position:absolute;left:0;right:0;top:262px;display:flex;justify-content:center;align-items:center;gap:6px}
.pager::before,.pager::after{content:"";width:110px;height:1px;background:#cdd2da}
.pager i{width:6px;height:6px;border-radius:50%;background:var(--red)}

.finale{height:304px;background:linear-gradient(var(--soft) 0,var(--soft) 88px,var(--navy-deep) 88px)}
.cta{position:absolute;left:190px;top:0;width:420px;height:130px;background:var(--red);text-align:center;padding-top:20px;z-index:2}
.cta h2{font-family:"Russo One",sans-serif;font-weight:400;color:#fff;font-size:24px;line-height:1.05;text-transform:uppercase}
.cta .call{display:inline-flex;gap:6px;align-items:center;background:#fff;font-size:10px;color:var(--navy);padding:7px 30px;margin-top:12px;border-radius:3px}
.cta .call b{color:var(--red);font-weight:600}
.footer-logo{position:absolute;left:105px;top:168px;width:106px;height:92px;background:#fff;border-radius:50px;display:flex;align-items:center;justify-content:center;gap:5px}
.footer-logo .dot{width:10px;height:10px;border-radius:50%;background:var(--red);flex:none}
.footer-logo span{font-family:"Russo One",sans-serif;font-size:11px;color:var(--navy);width:62px;line-height:1.1}
.fcol{position:absolute;top:160px;color:#cfd5e2;font-size:7px;line-height:1.9}
.fcol h4{color:var(--red);font-family:"Russo One",sans-serif;font-size:8px;font-weight:400;margin-bottom:4px}
.fcol li{list-style:none;display:flex;gap:5px;align-items:flex-start}
.fcol .here{color:var(--red)}
.accredit{position:absolute;left:480px;top:185px;width:70px;height:26px;background:#fff;border-radius:2px;display:flex;align-items:center;padding-left:5px}
.accredit i{width:14px;height:18px;background:#2a5e95}
.map{position:absolute;left:567px;top:162px;width:128px;height:82px;background:linear-gradient(135deg,#dfe7dd,#cfd9e6)}
.legal{position:absolute;left:105px;right:105px;top:282px;display:flex;justify-content:space-between;font-size:6.5px;color:#bfc6d4}
.social{display:flex;gap:8px}
.social i{width:9px;height:9px;background:#bfc6d4;border-radius:1px}
.social i.r{background:var(--red);border-radius:50%}

/* ========== tablet view ========== */
.view-tablet{position:absolute;left:152px;top:67px;width:648px;height:439px;background:#fff;overflow:hidden;border-radius:14px}
.tab-header{position:relative;height:51px;z-index:2}
.tab-header .brand{left:30px;width:102px;height:88px}
.tab-header .brand span{font-size:10.5px;width:58px}
.tab-nav{position:absolute;left:180px;top:0;height:51px;display:flex;align-items:center;gap:15px;font-size:7.5px;font-weight:500;color:var(--ink)}
.tab-nav .active{color:var(--red);text-decoration:underline}
.tab-nav .phone{margin-left:12px;display:flex;gap:4px;align-items:center}
.tab-nav .btn{margin-left:14px;padding:7px 13px}
.tab-hero{position:relative;height:315px;text-align:center}
.tab-hero .hero-photo{position:absolute;inset:0}
.tab-hero h1{position:relative;padding-top:92px;font-family:"Russo One",sans-serif;font-weight:400;color:#fff;font-size:31px;line-height:1.0;text-transform:uppercase}
.tab-hero h1 em{font-style:normal;color:var(--red)}
.tab-hero .btn{position:relative;background:#fff;color:var(--navy);margin-top:14px}

/* ========== mobile view ========== */
.view-mobile{position:absolute;left:860px;top:67px;width:196px;height:2686px;background:#fff;overflow:hidden;border-radius:14px}
.mob-header{position:relative;height:34px;z-index:2}
.mob-brand{position:absolute;left:10px;top:0;width:58px;height:48px;background:#fff;border-radius:0 0 28px 28px;display:flex;align-items:center;justify-content:center;gap:3px;box-shadow:0 2px 5px rgba(0,0,0,.12)}
.mob-brand i{width:6px;height:6px;border-radius:50%;background:var(--red);flex:none}
.mob-brand span{font-family:"Russo One",sans-serif;font-size:6.5px;color:var(--navy);line-height:1.1;width:36px}
.burger{position:absolute;right:10px;top:12px;width:14px;display:flex;flex-direction:column;gap:3px}
.burger i{height:1.5px;background:var(--ink)}
.mob-hero{position:relative;height:226px;text-align:center}
.mob-hero .hero-photo{position:absolute;inset:0}
.mob-hero h1{position:relative;padding-top:68px;font-family:"Russo One",sans-serif;font-weight:400;color:#fff;font-size:14.5px;line-height:1.15;text-transform:uppercase}
.mob-hero h1 em{font-style:normal;color:var(--red)}
.mob-hero .btn{position:relative;background:#fff;color:var(--navy);margin-top:10px;font-size:8px;padding:6px 12px}
.mob-abs{position:absolute}
.mob-pad{left:9px;width:178px}
.mob-title{font-size:17px;line-height:1.05}
.mob-text{font-size:8.5px;line-height:1.42;color:#3d4350}
.mob-services{position:absolute;left:0;top:714px;width:196px;height:1309px;background:var(--soft)}
.mob-sec-title{position:absolute;left:0;right:0;text-align:center;font-size:15px;line-height:1.0}
.mob-sec-title::before,.mob-sec-title::after{content:"";position:absolute;top:7px;width:14px;height:1px;background:#b9bdc6}
.mob-sec-title::before{left:12px}
.mob-sec-title::after{right:12px}
.mob-card{position:absolute;left:9px;width:178px}
.mob-card .card-img{height:134px}
.mob-card h3{font-size:10px;font-weight:600;color:var(--ink);margin:8px 0 1px}
.mob-card p{font-size:7.5px;line-height:1.3}
.field{position:absolute;left:9px;width:178px;height:20px;border:1px solid var(--line);font-size:6.5px;color:#9aa0aa;padding:5px 8px}
.submit{position:absolute;left:70px;top:2627px;width:56px;height:20px;background:var(--red);color:#fff;font-size:7.5px;font-weight:600;text-align:center;line-height:20px;border-radius:3px}
</style>
</head>
<body>

<!-- tablet view -->
<div class="view-tablet">
  <header class="tab-header">
    <div class="brand"><i class="dot"></i><span>YARDLINE WORKS</span></div>
    <nav class="tab-nav">
      <span class="active">Home</span><span>About Us</span><span>Services</span><span>Areas Served</span><span>Contact Us</span>
      <span class="phone"><svg width="8" height="8" viewBox="0 0 24 24"><path fill="#e3202a" d="M6.6 10.8a15 15 0 006.6 6.6l2.2-2.2c.3-.3.7-.4 1-.2 1.1.4 2.3.6 3.6.6.6 0 1 .4 1 1V20c0 .6-.4 1-1 1A17 17 0 013 4c0-.6.4-1 1-1h3.5c.6 0 1 .4 1 1 0 1.3.2 2.5.6 3.6.1.3 0 .7-.2 1z"/></svg>555 0148 273</span>
      <span class="btn">Get A Free Quote</span>
    </nav>
  </header>
  <div class="tab-hero">
    <div class="hero-photo" role="img" aria-label="Black wrought iron gate with a mounted mailbox in front of a brick house"></div>
    <h1>Yardline <em>Works</em><br>Fencing &amp; Gates<br>Company</h1>
    <span class="btn">Get A Free Quote</span>
  </div>
</div>

<!-- desktop view -->
<div class="view-desktop">

  <header class="site-header">
    <div class="brand"><i class="dot"></i><span>YARDLINE WORKS</span></div>
    <nav class="nav">
      <span class="active">Home</span><span>About Us</span><span>Services</span><span>Areas Served</span><span>Contact Us</span>
      <span class="phone"><svg width="8" height="8" viewBox="0 0 24 24"><path fill="#e3202a" d="M6.6 10.8a15 15 0 006.6 6.6l2.2-2.2c.3-.3.7-.4 1-.2 1.1.4 2.3.6 3.6.6.6 0 1 .4 1 1V20c0 .6-.4 1-1 1A17 17 0 013 4c0-.6.4-1 1-1h3.5c.6 0 1 .4 1 1 0 1.3.2 2.5.6 3.6.1.3 0 .7-.2 1z"/></svg>555 0148 273</span>
      <span class="btn">Get A Free Quote</span>
    </nav>
  </header>

  <section class="hero">
    <div class="hero-photo" role="img" aria-label="Black wrought iron gate with a mounted mailbox in front of a brick house"></div>
    <div class="hero-content">
      <h1>Yardline <em>Works</em><br>Fencing &amp; Gates<br>Company</h1>
      <span class="btn">Get A Free Quote</span>
    </div>
  </section>

  <section class="split about">
    <div class="deco pink hexv" style="left:0;top:55px;width:30px;height:64px"></div>
    <div class="container">
      <div class="copy">
        <h2 class="display">About <em>Us</em></h2>
        <p>Lorem Ipsum Is Simply Dummy Text Of The Printing And Typesetting Industry. Lorem Ipsum Has Been The Industry's Standard Dummy Text Ever Since The 1500s, When An Unknown Printer Took A Galley Of Type And Scrambled It To Make A Type Specimen Book. It Has Survived Not Only Five Centuries, But Also The Leap Into Electronic Typesetting, Remaining Essentially Unchanged.</p>
        <p>It Was Popularised In The 1960s With The Release Of Letraset Sheets Containing Lorem Ipsum Passages, And More Recently With Desktop Publishing Software Like Aldus PageMaker Including Versions Of Lorem Ipsum.</p>
        <span class="btn">Read More</span>
      </div>
      <div class="split-photo hex" role="img" aria-label="Fence installer in overalls kneeling with a power drill"></div>
      <div class="deco grey hexv" style="left:555px;top:22px;width:26px;height:30px"></div>
      <div class="deco pink hexv" style="left:520px;top:232px;width:22px;height:26px"></div>
      <div class="badge-20 hexv">20+</div>
      <div class="badge-label">YEAR OF<br>EXPERIENCE</div>
    </div>
  </section>

  <section class="services">
    <div class="container">
      <h2 class="sec-title display">Our <em>Services</em></h2>
      <div class="service-grid">
        <div class="card"><div class="card-img" role="img" aria-label="Grey horizontal slat fence in front of a house" style="background:linear-gradient(#9aa0a6,#3d4146)"></div><h3>Fence Installation</h3><p>Lorem Ipsum Is Simply Dummy Text<br>Of The Printing Industry.</p></div>
        <div class="card"><div class="card-img" role="img" aria-label="Black automatic sliding gate" style="background:linear-gradient(#6b7a5c,#26292d)"></div><h3>Automatic Gates</h3><p>Lorem Ipsum Is Simply Dummy Text<br>Of The Printing Industry.</p></div>
        <div class="card"><div class="card-img" role="img" aria-label="Welder fabricating a metal frame in a workshop" style="background:linear-gradient(#8a8f98,#2e3440)"></div><h3>Custom Fabrication</h3><p>Lorem Ipsum Is Simply Dummy Text<br>Of The Printing Industry.</p></div>
        <div class="card"><div class="card-img" role="img" aria-label="Workers in hard hats reviewing plans" style="background:linear-gradient(#b88a4a,#2f3d55)"></div><h3>Project Consulting</h3><p>Lorem Ipsum Is Simply Dummy Text<br>Of The Printing Industry.</p></div>
        <div class="card"><div class="card-img" role="img" aria-label="Hand fixing a dark metal fence panel with a drill" style="background:linear-gradient(90deg,#5d636b,#2b2f35)"></div><h3>Planned Gate Maintenance</h3><p>Lorem Ipsum Is Simply Dummy Text<br>Of The Printing Industry.</p></div>
        <div class="card"><div class="card-img" role="img" aria-label="Black pergola patio cover with a wooden roof" style="background:linear-gradient(#c9b48a,#2a2c2e)"><span class="arrow-dot hexv"><svg width="10" height="10" viewBox="0 0 24 24"><path fill="none" stroke="#fff" stroke-width="3" d="M4 12h15M13 6l6 6-6 6"/></svg></span></div><h3 class="hot">Pergolas &amp; Patio Covers</h3><p>Lorem Ipsum Is Simply Dummy Text<br>Of The Printing Industry.</p></div>
      </div>
      <div class="center-btn"><span class="btn">Contact Now</span></div>
    </div>
  </section>

  <section class="testimonials">
    <div class="deco grey hexv" style="right:0;top:85px;width:28px;height:56px;opacity:.5"></div>
    <div class="deco pink hexv" style="left:0;top:225px;width:42px;height:76px;opacity:.7"></div>
    <div class="container">
      <h2 class="sec-title display">Our Clients <em>Say</em></h2>
      <div class="quote-photo hex" role="img" aria-label="Glowing gear with a check mark and gold stars above an open hand"></div>
      <div class="quote">
        <div class="mark">&#8220;</div>
        <p>Lorem Ipsum is simply dummy text of the printing and typesetting industry. Lorem Ipsum has been the industry's standard dummy text ever since the 1500s, when an unknown printer took a galley of type and scrambled it to make a type specimen book. It has survived not only five centuries, but also the leap into electronic typesetting, remaining essentially unchanged.</p>
        <div class="author">
          <div class="avatar" role="img" aria-label="Client portrait"></div>
          <div><b>Maren Holt</b><small>Lorem Ipsum</small></div>
          <div class="dots"><i></i><i></i><i class="on"></i><i></i></div>
        </div>
      </div>
    </div>
  </section>

  <section class="works">
    <div class="container">
      <h2 class="sec-title display">Our <em>Works</em></h2>
    </div>
    <div class="work" style="left:105px;width:368px">
      <div role="img" aria-label="Black pavilion beside a sports field behind a mesh fence" style="height:100%;background:linear-gradient(#a9c3d8,#5d7a4c 70%,#8a5a3a)"></div>
      <div class="info"><h3>Lorem Ipsum Simply<br>Dummy Text</h3><p>Lorem Lorem Ipsum Is Simply Dummy Text Of The Printing And Typesetting Industry. Lorem Ipsum Has Been...</p><span class="go"><svg width="8" height="8" viewBox="0 0 24 24"><path fill="none" stroke="#fff" stroke-width="3" d="M4 12h15M13 6l6 6-6 6"/></svg></span></div>
    </div>
    <div class="work alt" style="left:491px;width:320px">
      <div role="img" aria-label="Horizontal red cedar slat fence on a concrete terrace" style="height:100%;background:linear-gradient(90deg,#b0542f,#7e3a20 45%,#c9c7c2 60%,#8c8c88)"></div>
      <div class="info"><h3>Lorem Ipsum Simply<br>Dummy Text</h3><p>Lorem Lorem Ipsum Is Simply Dummy Text Of The Printing And Typesetting Industry. Lorem Ipsum Has Been...</p></div>
    </div>
    <div class="center-btn"><span class="btn">View All</span></div>
  </section>

  <section class="split why">
    <div class="deco pink hexv" style="left:0;top:30px;width:28px;height:60px;opacity:.7"></div>
    <div class="container">
      <div class="copy" style="top:95px">
        <h2 class="display">Why<br>Choose <em>Us</em></h2>
        <p>Lorem Ipsum Is Simply Dummy Text Of The Printing And Typesetting Industry. Lorem Ipsum Has Been The Industry's Standard Dummy Text Ever Since The 1500s, When An Unknown Printer Took A Galley Of Type And Scrambled It To Make A Type Specimen Book. It Has Survived Not Only Five Centuries, But Also The Leap Into Electronic Typesetting, Remaining Essentially Unchanged.</p>
        <p>It Was Popularised In The 1960s With The Release Of Letraset Sheets Containing Lorem Ipsum Passages, And More Recently With Desktop Publishing Software Like Aldus PageMaker Including Versions Of Lorem Ipsum.</p>
        <span class="btn">Read More</span>
      </div>
      <div class="split-photo hex" role="img" aria-label="Worker drilling a metal fence post" style="background:linear-gradient(120deg,#d8dde3,#8c949c 50%,#5e8a4a)"></div>
      <div class="deco grey hexv" style="left:555px;top:22px;width:26px;height:30px"></div>
      <div class="deco pink hexv" style="left:520px;top:232px;width:22px;height:26px"></div>
      <div class="hexv" style="position:absolute;left:300px;top:185px;width:66px;height:74px;background:#fff;display:flex;align-items:center;justify-content:center;font-family:'Russo One',sans-serif;font-size:8px;color:var(--navy);text-align:center;line-height:1.1">YARDLINE<br>WORKS</div>
    </div>
  </section>

  <section class="clients">
    <div class="container">
      <h2 class="sec-title display">Our&nbsp;<em>Clients</em></h2>
      <div class="sub">Trusted By Top-Tier Companies Around The Globe</div>
      <div class="logo-row">
        <div class="logo-hex hex"><i style="background:#6cc08a"></i><span>LOREM</span></div>
        <div class="logo-hex hex"><i style="background:#e9a23b"></i><span>LOREM</span></div>
        <div class="logo-hex hex"><i style="background:#2f7ec4"></i><span>LOREM</span></div>
        <div class="logo-hex hex"><i style="background:#d8373a"></i><span>LOREM</span></div>
        <div class="logo-hex hex"><i style="background:#78b83f"></i><span>LOREM</span></div>
      </div>
    </div>
    <div class="pager"><i></i></div>
  </section>

  <footer class="finale">
    <div class="cta">
      <h2>Build Your<br>Fence Today!</h2>
      <div class="call">Call For Free Estimate <b>&#9742; 555 0148 273</b></div>
    </div>
    <div class="footer-logo"><i class="dot"></i><span>YARDLINE WORKS</span></div>
    <div class="fcol" style="left:282px">
      <h4>CONTACT US</h4>
      <ul>
        <li><span class="here">&#9742;</span>+1 555 0190 442</li>
        <li><span class="here">&#9993;</span>info@yardlineworks.example</li>
        <li><span class="here">&#9679;</span>12 Harlow Lane,<br>Fernvale, 9034</li>
      </ul>
    </div>
    <div class="fcol" style="left:382px">
      <h4>QUICK LINKS</h4>
      <ul><li class="here">Home</li><li>About Us</li><li>Services</li><li>Areas Served</li><li>Contact Us</li></ul>
    </div>
    <div class="accredit"><i></i></div>
    <div class="map" role="img" aria-label="Map of the service area"></div>
    <div class="legal"><span>© 2025 Yardline Works. All Rights Reserved.</span><span class="social"><i></i><i></i><i class="r"></i></span></div>
  </footer>
</div>

<!-- mobile view -->
<div class="view-mobile">
  <header class="mob-header">
    <div class="mob-brand"><i></i><span>YARDLINE WORKS</span></div>
    <div class="burger"><i></i><i></i><i></i></div>
  </header>
  <div class="mob-hero">
    <div class="hero-photo" role="img" aria-label="Black wrought iron gate in front of a brick house"></div>
    <h1>Yardline <em>Works</em><br>Fencing &amp; Gates<br>Company</h1>
    <span class="btn">Get A Free Quote</span>
  </div>

  <div class="mob-abs hex" role="img" aria-label="Fence installer in overalls kneeling with a power drill" style="left:30px;top:293px;width:150px;height:140px;background:linear-gradient(140deg,#7fa7c9,#c7a877 60%,#5b6a55)"></div>
  <div class="mob-abs hexv" style="left:138px;top:290px;width:22px;height:25px;background:var(--grey-hex)"></div>
  <div class="mob-abs hexv" style="left:133px;top:425px;width:24px;height:28px;background:var(--pink)"></div>
  <div class="mob-abs hexv" style="left:20px;top:380px;width:50px;height:56px;background:var(--red);color:#fff;font-family:'Russo One',sans-serif;font-size:16px;display:flex;align-items:center;justify-content:center">20+</div>
  <div class="mob-abs" style="left:20px;top:448px;font-family:'Russo One',sans-serif;font-size:7.5px;line-height:1.1;color:var(--ink)">YEAR OF<br>EXPERIENCE</div>
  <h2 class="mob-abs mob-pad display mob-title" style="top:486px">About <em>Us</em></h2>
  <p class="mob-abs mob-pad mob-text" style="top:512px">Lorem Ipsum Is Simply Dummy Text Of The Printing And Typesetting Industry. Lorem Ipsum Has Been The Industry's Standard Dummy Text Ever Since The 1500s, When An Unknown Printer Took A Galley Of Type And Scrambled It To Make A Type Specimen Book. It Has Survived Not Only Five Centuries, But Also The Leap Into Electronic Typesetting, Remaining Essentially Unchanged.</p>
  <span class="mob-abs btn" style="left:9px;top:655px;font-size:8px;padding:6px 14px">Read More</span>

  <div class="mob-services">
    <h2 class="mob-sec-title display" style="top:34px">Our<br><em>Services</em></h2>
    <div class="mob-card" style="top:73px"><div class="card-img" role="img" aria-label="Grey horizontal slat fence" style="background:linear-gradient(#9aa0a6,#3d4146)"></div><h3>Fence Installation</h3><p>Lorem Ipsum Is Simply Dummy Text<br>Of The Printing Industry.</p></div>
    <div class="mob-card" style="top:271px"><div class="card-img" role="img" aria-label="Black automatic sliding gate" style="background:linear-gradient(#6b7a5c,#26292d)"></div><h3>Automatic Gates</h3><p>Lorem Ipsum Is Simply Dummy Text<br>Of The Printing Industry.</p></div>
    <div class="mob-card" style="top:469px"><div class="card-img" role="img" aria-label="Welder fabricating a metal frame" style="background:linear-gradient(#8a8f98,#2e3440)"></div><h3>Custom Fabrication</h3><p>Lorem Ipsum Is Simply Dummy Text<br>Of The Printing Industry.</p></div>
    <div class="mob-card" style="top:667px"><div class="card-img" role="img" aria-label="Workers in hard hats reviewing plans" style="background:linear-gradient(#b88a4a,#2f3d55)"></div><h3>Project Consulting</h3><p>Lorem Ipsum Is Simply Dummy Text<br>Of The Printing Industry.</p></div>
    <div class="mob-card" style="top:865px"><div class="card-img" role="img" aria-label="Hand fixing a dark metal fence panel" style="background:linear-gradient(90deg,#5d636b,#2b2f35)"></div><h3>Planned Gate Maintenance</h3><p>Lorem Ipsum Is Simply Dummy Text<br>Of The Printing Industry.</p></div>
    <div class="mob-card" style="top:1063px"><div class="card-img" role="img" aria-label="Black pergola patio cover" style="background:linear-gradient(#c9b48a,#2a2c2e)"></div><h3>Pergolas &amp; Patio Covers</h3><p>Lorem Ipsum Is Simply Dummy Text</p></div>
    <span class="mob-abs btn" style="left:62px;top:1240px;font-size:7.5px;padding:6px 12px">Contact Now</span>
  </div>

  <h2 class="mob-sec-title display" style="top:2050px">Our Clients<br><em>Say</em></h2>
  <div class="mob-abs" style="left:9px;top:2100px;font-family:'Russo One',sans-serif;color:var(--red);font-size:26px;line-height:1">&#8220;</div>
  <p class="mob-abs mob-pad" style="top:2130px;font-size:8.5px;line-height:1.5;color:#3d4350">Lorem Ipsum is simply dummy text of the printing and typesetting industry. Lorem Ipsum has been the industry's standard dummy text ever since the 1500s, when an unknown printer took a galley of type and scrambled it to make a type specimen book. It has survived not only five centuries, but also the leap into electronic typesetting, remaining essentially unchanged.</p>
  <div class="mob-abs author" style="left:9px;top:2290px;margin:0">
    <div class="avatar" role="img" aria-label="Client portrait"></div>
    <div><b>Maren Holt</b><small>Lorem Ipsum</small></div>
  </div>
  <div class="mob-abs dots" style="left:75px;top:2335px"><i></i><i></i><i class="on"></i><i></i></div>

  <h2 class="mob-abs display" style="left:0;right:0;top:2398px;text-align:center;font-size:14px"><em>Quick Inquiry</em></h2>
  <div class="field" style="top:2436px">First Name</div>
  <div class="field" style="top:2465px">Last Name</div>
  <div class="field" style="top:2494px">Phone</div>
  <div class="field" style="top:2523px">Email</div>
  <div class="field" style="top:2552px;height:54px">How Can We Help?</div>
  <div class="submit">SUBMIT</div>
</div>

</body>
</html>
```